Mailer Postcard for Potential Bankruptcy Clients

The postcard will be printed at 8.5"x6" to abide by the specification at the following link: https://www.mailtrelbo.com/submitting-art/specs/. I want an attractive two sided post card that includes my logo (see attachment). The design would have to have room for the website address, phone number, two location addresses and give them information about a civil action pending against them (You are being sued in X county (case# xxyx). We can help.). I don't really like the visuals of the attached postcard, so please use as a general guide for what I am trying to do. Ultimately, I want an ad that gets people to call me so I can help them.

I also want it to be compatible with the website (LoanHarbor.Legal).

Target Market(s)

Potential bankruptcy clients.

Industry/Entity Type

Legal

Colors

Designer to choose colors to be used in the design.

Requirements
Must have
• Phone number, addresses, website, and place for text regarding pending legal action against the receiver. Should say something to the effect: You have a pending legal action in (county name) County (court name [superior, magistrate, ect.]). Let us help you deal with it responsibly.
• Please note the design specifications at this link:

```html
<!DOCTYPE html>
<html lang="en">
<head>
<meta charset="utf-8">
<title>Loan Harbor Law Group – Mailer Postcard</title>
<link rel="stylesheet" href="https://fonts.googleapis.com/css2?family=Montserrat:wght@400;500;600;700;800&family=Raleway:wght@300;400;500&display=swap">
<style>
  :root {
    --page-bg: #e9eaec;
    --card-white: #ffffff;
    --brand-green: #6dbb7a;
    --brand-green-deep: #3fae7e;
    --charcoal: #3b3e42;
    --ink: #2b2d30;
    --ink-soft: #55585c;
    --night: #121518;
  }
  * { box-sizing: border-box; margin: 0; padding: 0; }
  html, body {
    width: 970px; height: 1200px; overflow: hidden;
    background: var(--page-bg);
    font-family: "Montserrat", sans-serif;
    color: var(--ink);
  }
  .sheet { position: relative; width: 970px; height: 1200px; }
  .postcard {
    position: absolute; left: 95px; width: 780px; height: 551px;
    background: var(--card-white); overflow: hidden;
    box-shadow: 0 6px 18px rgba(0,0,0,.22);
  }
  .postcard--front { top: 30px; }
  .postcard--back { top: 619px; }
  .card-art { position: absolute; inset: 0; width: 780px; height: 551px; display: block; }

  /* brand lockup: name set in one colour / one weight */
  .brand-dot { position: absolute; border-radius: 50%; background: var(--brand-green); }
  .brand-name {
    position: absolute; font-family: "Raleway", sans-serif; font-weight: 500;
    color: var(--charcoal); line-height: 1.1; letter-spacing: .5px;
  }
  .postcard--front .brand-dot { left: 98px; top: 28px; width: 100px; height: 100px; }
  .postcard--front .brand-name { left: 48px; top: 150px; width: 200px; text-align: center; font-size: 28px; }
  .postcard--back .brand-dot { left: 226px; top: 28px; width: 48px; height: 48px; }
  .postcard--back .brand-divider { position: absolute; left: 286px; top: 22px; width: 2px; height: 66px; background: var(--charcoal); }
  .postcard--back .brand-name { left: 298px; top: 30px; font-size: 19px; }

  /* front headline */
  .question-mark {
    position: absolute; left: 22px; top: 368px; font-family: "Montserrat", sans-serif;
    font-weight: 800; font-size: 150px; line-height: 1; color: #fff;
  }
  .headline-lead {
    position: absolute; left: 93px; top: 372px; font-weight: 500; font-size: 29px;
    color: #fff; letter-spacing: .3px;
  }
  .headline-band {
    position: absolute; left: 93px; top: 413px; width: 500px; height: 50px;
    background: linear-gradient(90deg, var(--brand-green-deep), var(--brand-green));
  }
  .headline-main {
    position: absolute; left: 103px; top: 414px; font-weight: 800; font-size: 42px;
    color: #fff; letter-spacing: .3px; line-height: 48px;
  }
  .case-number {
    position: absolute; left: 93px; top: 468px; font-family: "Raleway", sans-serif;
    font-weight: 400; font-size: 24px; color: #fff;
  }
  .website {
    position: absolute; font-family: "Raleway", sans-serif; font-size: 16px; color: var(--ink);
  }
  .website b { font-family: "Montserrat", sans-serif; font-weight: 700; }
  .postcard--front .website { left: 340px; top: 517px; width: 200px; text-align: center; }
  .postcard--back .website { right: 15px; top: 520px; font-size: 14px; }

  /* back message */
  .notice { position: absolute; left: 26px; top: 84px; width: 320px; text-align: center; }
  .notice-intro { text-align: left; font-family: "Raleway", sans-serif; font-size: 24px; padding-left: 4px; line-height: 1.1; }
  .notice-action { text-align: left; font-weight: 700; font-size: 27px; color: var(--brand-green); line-height: 1.1; }
  .notice-court { font-family: "Raleway", sans-serif; font-size: 20px; padding-left: 40px; line-height: 1.3; }
  .notice-help { font-weight: 600; font-size: 21px; text-align: left; line-height: 1.2; }
  .notice-close { font-weight: 700; font-size: 38px; color: var(--brand-green); padding-left: 60px; line-height: 1.1; }

  .contact-pill {
    position: absolute; left: 104px; top: 260px; width: 190px; height: 26px; border-radius: 13px;
    background: var(--charcoal); color: var(--brand-green); font-weight: 500; font-size: 17px;
    text-align: center; line-height: 26px; letter-spacing: .5px;
  }
  .address-list { position: absolute; left: 30px; top: 302px; list-style: none; }
  .address-item { position: relative; padding-left: 28px; font-family: "Raleway", sans-serif; font-size: 13.5px; line-height: 18px; margin-bottom: 6px; color: var(--ink); }
  .address-item svg { position: absolute; left: 2px; top: 2px; width: 14px; height: 16px; }
  .call-line { position: absolute; left: 44px; top: 388px; white-space: nowrap; }
  .call-label { font-size: 15px; font-weight: 500; }
  .call-number { font-size: 29px; font-weight: 600; color: var(--ink); margin-left: 4px; }

  .stamp-box { position: absolute; left: 667px; top: 14px; width: 98px; height: 92px; border: 1.5px solid var(--ink-soft); }
  .address-rule { position: absolute; left: 446px; width: 319px; height: 1.5px; background: var(--ink-soft); }
</style>
</head>
<body>
<main class="sheet">

  <!-- Front side -->
  <section class="postcard postcard--front" aria-label="Postcard front">
    <svg class="card-art" viewBox="0 0 780 551" aria-hidden="false">
      <defs>
        <linearGradient id="deskPhoto" x1="0" y1="1" x2="1" y2="0">
          <stop offset="0" stop-color="#0f1215"/>
          <stop offset=".45" stop-color="#2c3035"/>
          <stop offset=".65" stop-color="#8b8f92"/>
          <stop offset=".85" stop-color="#3b3f45"/>
          <stop offset="1" stop-color="#1f2227"/>
        </linearGradient>
        <linearGradient id="gavelPhoto" x1="0" y1="0" x2="1" y2="1">
          <stop offset="0" stop-color="#d9d2c6"/>
          <stop offset=".5" stop-color="#8a5a36"/>
          <stop offset="1" stop-color="#f0ece4"/>
        </linearGradient>
      </defs>
      <rect role="img" aria-label="Photo: an attorney's hand pressing a seal stamp onto a certificate on a desk" width="780" height="551" fill="url(#deskPhoto)"/>
      <path d="M0,0 H545 C500,150 330,258 0,268 Z" fill="var(--card-white)"/>
      <path d="M545,0 C500,150 330,258 0,268 L0,296 C360,286 530,160 580,0 Z" fill="var(--brand-green)"/>
      <path d="M580,0 C530,160 360,286 0,296 L0,312 C370,302 545,170 596,0 Z" fill="#4a4d52"/>
      <circle cx="408" cy="140" r="100" fill="var(--card-white)" stroke="var(--brand-green)" stroke-width="4"/>
      <circle role="img" aria-label="Photo: a wooden gavel resting beside a closed law book" cx="408" cy="140" r="89" fill="url(#gavelPhoto)"/>
      <path d="M215,551 C320,488 610,480 710,551 Z" fill="var(--brand-green)"/>
    </svg>

    <div class="brand-dot" aria-hidden="true"></div>
    <p class="brand-name">Loan Harbor<br>Law Group</p>

    <span class="question-mark" aria-hidden="true">?</span>
    <p class="headline-lead">ARE YOU BEING</p>
    <div class="headline-band" aria-hidden="true"></div>
    <h1 class="headline-main">SUED IN X COUNTY</h1>
    <p class="case-number">(CASE# XXYX)</p>
    <p class="website">www.<b>loanharbor</b>.legal</p>
  </section>

  <!-- Back side -->
  <section class="postcard postcard--back" aria-label="Postcard back">
    <svg class="card-art" viewBox="0 0 780 551">
      <defs>
        <linearGradient id="skyPhoto" x1="0" y1="0" x2="0" y2="1">
          <stop offset="0" stop-color="#ffffff" stop-opacity="0"/>
          <stop offset=".35" stop-color="#e8ebe6"/>
          <stop offset=".75" stop-color="#efe6c8"/>
          <stop offset="1" stop-color="#b9b49f"/>
        </linearGradient>
      </defs>
      <rect role="img" aria-label="Photo: a man standing with arms spread wide against a bright open sky" x="0" y="400" width="470" height="151" fill="url(#skyPhoto)"/>
      <path d="M588,0 C450,110 395,300 432,551 L780,551 L780,0 Z" fill="var(--brand-green)"/>
      <path d="M614,0 C482,120 430,310 462,551 L780,551 L780,0 Z" fill="#4a4d52"/>
      <path d="M624,0 C494,122 442,312 474,551 L780,551 L780,0 Z" fill="var(--card-white)"/>
    </svg>

    <div class="brand-dot" aria-hidden="true"></div>
    <div class="brand-divider" aria-hidden="true"></div>
    <p class="brand-name">Loan Harbor<br>Law Group</p>

    <div class="notice">
      <p class="notice-intro">You have a</p>
      <p class="notice-action">pending legal action</p>
      <p class="notice-court">in County magistrate</p>
      <p class="notice-help">Let us help you deal with it</p>
      <p class="notice-close">responsibly.</p>
    </div>

    <p class="contact-pill">GET IN TOUCH</p>
    <ul class="address-list">
      <li class="address-item">
        <svg viewBox="0 0 14 16" aria-hidden="true"><path d="M7,0 C3,0 0,3 0,6.5 C0,11 7,16 7,16 C7,16 14,11 14,6.5 C14,3 11,0 7,0 Z" fill="var(--brand-green)"/><circle cx="7" cy="6.5" r="2.6" fill="#fff"/></svg>
        418 Linden Ave. NW Suite #1400 Atlanta,<br>Georgia 30308
      </li>
      <li class="address-item">
        <svg viewBox="0 0 14 16" aria-hidden="true"><path d="M7,0 C3,0 0,3 0,6.5 C0,11 7,16 7,16 C7,16 14,11 14,6.5 C14,3 11,0 7,0 Z" fill="var(--brand-green)"/><circle cx="7" cy="6.5" r="2.6" fill="#fff"/></svg>
        5120 Maple Ridge Rd. Douglasville,<br>Georgia 30135
      </li>
    </ul>
    <p class="call-line"><span class="call-label">Call now:</span> <span class="call-number">(404) 555-0172</span></p>

    <div class="stamp-box" aria-hidden="true"></div>
    <div class="address-rule" style="top:260px" aria-hidden="true"></div>
    <div class="address-rule" style="top:308px" aria-hidden="true"></div>
    <div class="address-rule" style="top:357px" aria-hidden="true"></div>

    <p class="website">www.<b>loanharbor</b>.legal</p>
  </section>

</main>
</body>
</html>
```